Harbor Bug Guard Business Cards

A modern business card with a predominantly white background and a sleek design featuring Harbor with complimentary greys or blacks to convey a professional and contemporary look.

Front:
Primarily white background. Limited use of company purple color can be neighbored by greys.
Text: Name, Title, Cell Phone, Office Phone, Website, email address

Back:
Background Continuation: The back of the card maintains the white background for consistency.
Company name “Harbor” in company color and font, “Bug Guard” underneath or underneath left justified of “Harbor.”
A subtle pattern or texture in shades of grey to add depth behind the company Logo in font.

logo color: hex #6212ab
font: antique olive nord D Regular

```html
<!DOCTYPE html>
<html lang="en">
<head>
<meta charset="utf-8">
<title>Harbor Bug Guard Business Cards</title>
<link rel="stylesheet" href="https://fonts.googleapis.com/css2?family=Archivo:wdth,wght@62..125,100..900&display=swap">
<style>
  :root {
    --brand: #6212ab;
    --ink-grey: #6f6f6f;
    --card: #f3f3f3;
    --stage: #2b2b2b;
    --card-w: 640px;
    --card-h: 366px;
  }
  * { box-sizing: border-box; margin: 0; padding: 0; }
  html, body {
    width: 1200px;
    height: 1015px;
    overflow: hidden;
    background: var(--stage);
  }
  .stage {
    position: relative;
    width: 1200px;
    height: 1015px;
    display: flex;
    flex-direction: column;
    align-items: center;
    justify-content: center;
    gap: 70px;
  }
  .card {
    position: relative;
    width: var(--card-w);
    height: var(--card-h);
    background: var(--card);
    box-shadow: 0 10px 28px rgba(0,0,0,.45);
    font-family: "Archivo", "Arial Black", sans-serif;
    font-stretch: 125%;
    font-weight: 900;
    overflow: hidden;
  }
  .card-texture {
    position: absolute;
    inset: 0;
    width: 100%;
    height: 100%;
  }
  .card-frame {
    position: absolute;
    inset: 34px 48px;
    border: 1.5px solid var(--brand);
  }
  .logo-side .wordmark {
    position: absolute;
    left: 50%;
    top: 50%;
    transform: translate(-50%, -54%);
    color: var(--brand);
    line-height: .9;
  }
  .wordmark-main {
    display: block;
    font-size: 78px;
    letter-spacing: -1px;
  }
  .wordmark-sub {
    display: block;
    font-size: 33px;
    margin-top: 6px;
    padding-left: 34px;
  }
  .contact-side .details {
    position: absolute;
    left: 50%;
    top: 50%;
    transform: translate(-50%, -50%);
    text-align: center;
    color: var(--ink-grey);
    font-size: 19px;
    line-height: 1.2;
  }
  .person-name {
    color: var(--brand);
    font-size: 21px;
    text-transform: uppercase;
  }
  .divider {
    width: 110px;
    height: 1px;
    background: var(--brand);
    margin: 14px auto;
  }
</style>
</head>
<body>
<main class="stage">
  <section class="card logo-side">
    <svg class="card-texture" aria-hidden="true">
      <filter id="paper-grain">
        <feTurbulence type="fractalNoise" baseFrequency="1.2" numOctaves="2"/>
        <feColorMatrix values="0 0 0 0 0.55  0 0 0 0 0.55  0 0 0 0 0.55  0 0 0 0.18 0"/>
      </filter>
      <rect width="100%" height="100%" filter="url(#paper-grain)"/>
    </svg>
    <div class="card-frame"></div>
    <h1 class="wordmark">
      <span class="wordmark-main">Harbor</span>
      <span class="wordmark-sub">Bug Guard</span>
    </h1>
  </section>

  <section class="card contact-side">
    <svg class="card-texture" aria-hidden="true">
      <rect width="100%" height="100%" filter="url(#paper-grain)"/>
    </svg>
    <div class="card-frame"></div>
    <div class="details">
      <p class="person-name">Daniel Brooks</p>
      <p class="person-title">Managing Director</p>
      <div class="divider"></div>
      <p class="phone">044-555 210 347</p>
      <p class="phone">044-555 210 348</p>
      <div class="divider"></div>
      <p class="email">info@harborbug.com</p>
      <p class="website">www.harborbugguard.com</p>
    </div>
  </section>
</main>
</body>
</html>
```